Redesign Business Cards, Attached

Please read instructions carefully. If you have any questions send a message before submitting your ONE design. Please redesign attached business cards. Double sided. Use same content and descriptions. Use black, silver, crimson red and gold colors. My only issue with the attached design is the background colors. I like the layout as-is. I can provide the individual pictures on the back side later. Do not submit more than one design. One submission shall include both front and back. Do not submit front and back separately. A second project will be launched to create a matching post card after completion of this.
Industry/Entity Type
see description and attachments.
Contact Information for Business Card
Requirements
Must have
- see description and attachments.
Nice to have
Should not have

```html
<!DOCTYPE html>
<html lang="en">
<head>
<meta charset="utf-8">
<title>Harbor Helm Business Cards</title>
<link rel="stylesheet" href="https://fonts.googleapis.com/css2?family=Poppins:wght@500;600&family=Roboto:ital,wght@1,300;1,400&display=swap">
<style>
  :root{
    --stage:#d4d5d7;
    --graphite:#2a2c30;
    --graphite-deep:#141517;
    --silver-light:#e3e5e8;
    --silver:#b9bdc3;
    --silver-deep:#7f848b;
    --gold:#d2a72a;
    --gold-deep:#a9861f;
    --black:#0b0b0c;
    --crimson:#9e1b20;
    --pill:#b3181f;
    --white:#ffffff;
    --ink:#1a1a1a;
    --badge-blue:#1f4f94;
  }
  *{box-sizing:border-box;margin:0;padding:0}
  html,body{width:900px;height:1200px;overflow:hidden;background:var(--stage)}
  .stage{position:relative;width:900px;height:1200px}
  .card{position:absolute;left:135px;width:630px;overflow:hidden;box-shadow:6px 8px 12px rgba(0,0,0,.28)}
  .card--front{top:215px;height:357px;background:var(--white)}
  .card--back{top:628px;height:359px}
  .card svg.bg{position:absolute;inset:0}
  .brand-seal{position:absolute;border-radius:50%;background:var(--white);display:flex;align-items:center;justify-content:center;text-align:center;
    font-family:'Poppins',sans-serif;font-weight:600;color:var(--ink);line-height:1.15;box-shadow:0 0 0 4px var(--gold)}
  .services{position:absolute;inset:0}
  .tile{position:absolute;width:122px;height:70px;display:flex;align-items:center;justify-content:center;text-align:center;
    font-family:'Roboto',sans-serif;font-style:italic;font-weight:300;font-size:14px;line-height:1.22}
  .tile::before{content:"";position:absolute;inset:0;transform:skewX(-13deg);transform-origin:bottom;z-index:0}
  .tile span{position:relative;z-index:1}
  .tile--black{color:var(--white)} .tile--black::before{background:var(--black);box-shadow:0 0 0 1px rgba(255,255,255,.08)}
  .tile--gold{color:var(--ink);font-weight:400} .tile--gold::before{background:var(--gold)}
  .site{position:absolute;top:322px;left:0;width:100%;text-align:center;font-family:'Poppins',sans-serif;font-weight:600;font-size:17px;color:var(--ink);letter-spacing:.3px}
  .badge{position:absolute;border-radius:50%}
  .badge--council{left:46px;top:223px;width:76px;height:76px;background:var(--badge-blue);box-shadow:0 0 0 4px var(--white)}
  .badge--veteran{left:170px;top:234px;width:80px;height:80px;background:var(--crimson);box-shadow:0 0 0 4px var(--white)}
  .badge-caption{position:absolute;left:40px;top:320px;width:86px;text-align:center;font-family:'Poppins',sans-serif;font-weight:600;font-size:12px;color:var(--badge-blue)}
  .contact{position:absolute;left:365px;top:62px;font-family:'Poppins',sans-serif;color:var(--white)}
  .contact .name{font-size:23px;font-weight:600;color:var(--gold);letter-spacing:.2px}
  .contact .role{font-size:17.5px;font-weight:500;line-height:25px;letter-spacing:.4px;margin-top:2px}
  .pill{position:absolute;left:365px;top:191px;width:226px;height:34px;border-radius:17px;background:var(--pill);color:var(--white);
    font-family:'Poppins',sans-serif;font-weight:500;font-size:17px;display:flex;align-items:center;justify-content:center;gap:5px}
  .line{position:absolute;left:365px;display:flex;align-items:center;gap:7px;font-family:'Poppins',sans-serif;font-size:15px;color:var(--white);letter-spacing:.2px}
  .line--mail{top:237px} .line--web{top:270px}
</style>
</head>
<body>
<div class="stage">

  <section class="card card--front">
    <svg class="bg" width="630" height="357" viewBox="0 0 630 357">
      <defs>
        <linearGradient id="bandTone" x1="0" y1="0" x2="1" y2="1">
          <stop offset="0" stop-color="var(--graphite)"/><stop offset="1" stop-color="var(--graphite-deep)"/>
        </linearGradient>
        <linearGradient id="silverTone" x1="0" y1="0" x2="1" y2="1">
          <stop offset="0" stop-color="var(--silver-deep)"/><stop offset=".55" stop-color="var(--silver)"/><stop offset="1" stop-color="var(--silver-light)"/>
        </linearGradient>
      </defs>
      <rect x="0" y="0" width="630" height="200" fill="url(#bandTone)"/>
      <polygon points="288,0 331,0 305,38" fill="var(--crimson)"/>
      <polygon points="331,0 630,0 630,200 330,200 315,152 281,88" fill="url(#silverTone)" role="img" aria-label="Silver-toned photo of a white powerboat speeding across open water"/>
    </svg>
    <div class="brand-seal" style="left:99px;top:30px;width:116px;height:116px;font-size:13px">Harbor Helm<br>Boat Training<br>&amp; Charters</div>
    <div class="services">
      <div class="tile tile--black" style="left:90px;top:156px"><span>Hands-On<br>Boat<br>Training</span></div>
      <div class="tile tile--gold" style="left:218px;top:156px"><span>Introduction<br>to Power<br>boating</span></div>
      <div class="tile tile--black" style="left:343px;top:156px"><span>Precision<br>Docking &amp;<br>Boat Handling</span></div>
      <div class="tile tile--gold" style="left:468px;top:156px"><span>Open Water<br>Boat<br>Handling</span></div>
      <div class="tile tile--gold" style="left:64px;top:233px"><span>Island<br>Anchoring</span></div>
      <div class="tile tile--black" style="left:189px;top:233px"><span>Open Water<br>Advanced<br>Maneuvers</span></div>
      <div class="tile tile--gold" style="left:313px;top:233px"><span>Coastal<br>Navigation</span></div>
      <div class="tile tile--black" style="left:440px;top:233px"><span>Captaining/<br>Piloting Service<br>for Your Outings</span></div>
    </div>
    <div class="site">www.HelmHireBoats.com</div>
  </section>

  <section class="card card--back">
    <svg class="bg" width="630" height="359" viewBox="0 0 630 359">
      <defs>
        <linearGradient id="goldTone" x1="0" y1="0" x2="1" y2="1">
          <stop offset="0" stop-color="#c9a43a"/><stop offset=".5" stop-color="#b8942c"/><stop offset="1" stop-color="var(--gold-deep)"/>
        </linearGradient>
      </defs>
      <rect width="630" height="359" fill="url(#goldTone)" role="img" aria-label="Gold-toned water surface texture"/>
      <polygon points="290,0 360,0 308,88 265,40" fill="var(--crimson)"/>
      <polygon points="265,319 308,271 360,359 290,359" fill="var(--crimson)"/>
      <polygon points="355,0 630,0 630,359 355,359 250,180" fill="var(--white)"/>
      <polygon points="366,0 630,0 630,359 366,359 261,180" fill="var(--black)"/>
    </svg>
    <div class="brand-seal" style="left:81px;top:44px;width:132px;height:132px;font-size:14px">Harbor Helm<br>Boat Training<br>&amp; Charters</div>
    <div class="badge badge--council" role="img" aria-label="Boating safety council instructor badge"></div>
    <div class="badge badge--veteran" role="img" aria-label="Veteran-owned business verified badge"></div>
    <div class="badge-caption">INSTRUCTOR</div>
    <div class="contact">
      <div class="name">DALTON R. KEANE</div>
      <div class="role">USCG Licensed Captain<br>Certified Instructor</div>
    </div>
    <div class="pill">TEXT
      <svg width="16" height="16" viewBox="0 0 24 24" aria-hidden="true"><path fill="#fff" d="M6.6 10.8a15.1 15.1 0 0 0 6.6 6.6l2.2-2.2c.3-.3.7-.4 1-.2 1.1.4 2.3.6 3.6.6.6 0 1 .4 1 1V20c0 .6-.4 1-1 1A17 17 0 0 1 3 4c0-.6.4-1 1-1h3.5c.6 0 1 .4 1 1 0 1.3.2 2.5.6 3.6.1.3 0 .7-.2 1z"/></svg>
      (555) 014-2290</div>
    <div class="line line--mail">
      <svg width="17" height="13" viewBox="0 0 17 13" aria-hidden="true"><rect width="17" height="13" fill="var(--gold)"/><path d="M0 0l8.5 7L17 0" stroke="var(--black)" stroke-width="1.5" fill="none"/></svg>
      hello@helmhireboats.com</div>
    <div class="line line--web">
      <svg width="16" height="16" viewBox="0 0 16 16" aria-hidden="true"><circle cx="8" cy="8" r="7.5" fill="var(--gold)"/><path d="M1 8h14M8 1c3 3 3 11 0 14M8 1c-3 3-3 11 0 14" stroke="var(--black)" stroke-width="1" fill="none"/></svg>
      www.HelmHireBoats.com</div>
  </section>

</div>
</body>
</html>
```